Help our pizza bases / flat breads fly off the shelves - You'll be seen in supermarkets New Zealand

Packaging design.
We have bought a product that is in desperate need of a complete re-brand. This includes a name, and a package design.
It is an rectangle shaped flat bread that can be used in many ways, and is presented 5 in a pack, in an unprinted flexible formed bottom, with a flat top film applied that is flat and ready to receive your design.
The product is mainly used as a pizza base bought by Mums to feed the family. It is also can be a pre dinner nibble like a pizza bread, and for quick and easy, you can cut one into 3 pieces, and toast in a pop-up toaster, before topping with whatever is in your fridge.
The current name is "Kelmo breads" which is just silly. The brand "Kelmo" needs to change to "Dugald's Flat Breads" or whatever you might suggest. The product name might be "Tavira Pizza Base" or "Tavira Flat bread" as you like.
The look must get consumers to pick up the product and have a closer look. The nature of the graphics should emphasize the versatility and multi-usefulness, so the consumer can imagine what they will do with the product when they get it home. I feel that an informative pack will be better than a beautiful pack to get more sales. I have uploaded pictures showing the product currently in Supermarkets, and also a picture of the current product. Dimensions are 310 x 130mm.
You will need to leave room for: Barcode, Nutritional Panel, Cooking instructions, Storage instructions, Ingredients list and Company contact details - each one say 45 x 45mm or similar.
These details could go on the bottom of the low long side, as this is obscured while on shelf (see photo)
You will also highlight in your design, Preservative Free, 100% Natural, 5 Bases, Made with Olive oil, Hand made, and the variant (Roasted Garlic, or Original)
You will want to highlight the uses like: Pizza base, pizza bread, cut toast and top or similar.

```html
<!DOCTYPE html>
<html lang="en">
<head>
<meta charset="utf-8">
<title>Dugald's Breads – Pack Label</title>
<link href="https://fonts.googleapis.com/css2?family=Abril+Fatface&family=Oswald:wght@500;600&family=Roboto:wght@500;700&display=swap" rel="stylesheet">
<style>
  :root {
    --maroon: #6b1f15;
    --maroon-deep: #4a130d;
    --maroon-mid: #7c2a1e;
    --parchment: #fde8c8;
    --cream-border: #f6e7c9;
    --barcode-fill: #ffd9a0;
    --bg-light: #f4f4f4;
    --bg-dark: #dedede;
    --white: #ffffff;
  }
  * { margin: 0; padding: 0; box-sizing: border-box; }
  html, body { width: 1200px; height: 857px; overflow: hidden; }
  body {
    background: radial-gradient(ellipse at 50% 40%, var(--bg-light) 0%, var(--bg-dark) 100%);
    font-family: "Roboto", sans-serif;
    color: var(--maroon);
    position: relative;
  }
  .label {
    position: absolute;
    left: 55px; top: 200px;
    width: 1092px; height: 458px;
    background: radial-gradient(ellipse at 50% 45%, var(--maroon-mid) 0%, var(--maroon-deep) 100%);
    border: 2px solid var(--cream-border);
    box-shadow: 0 2px 6px rgba(0,0,0,0.2);
  }
  .parchment {
    position: absolute;
    left: 0; top: 0;
    width: 1092px; height: 458px;
    filter: drop-shadow(0 0 6px rgba(255,235,210,0.7));
  }
  .panel { position: absolute; }
  .heading {
    font-weight: 700; font-size: 9px; text-transform: uppercase;
    text-align: center; margin-bottom: 7px;
  }
  .copy {
    font-weight: 500; font-size: 8.8px; line-height: 12px;
    text-align: justify; text-align-last: center; margin-bottom: 5px;
  }
  .copy b { font-weight: 700; }
  .contact { left: 76px; top: 76px; width: 236px; }
  .brand-mini {
    position: absolute; left: 90px; top: 252px; width: 210px;
    font-family: "Abril Fatface", serif; font-size: 18px; line-height: 18px;
    text-align: center;
  }
  .barcode-area {
    position: absolute; left: 96px; top: 308px;
    width: 195px; height: 89px; background: var(--barcode-fill);
    display: flex; align-items: center; justify-content: center;
    font-family: "Abril Fatface", serif; font-size: 15px;
  }
  .count {
    position: absolute; left: 654px; top: 78px; width: 50px;
    text-align: center; font-family: "Oswald", sans-serif; font-weight: 600;
  }
  .count .num { font-size: 48px; line-height: 50px; display: block; }
  .count .unit { font-size: 13px; line-height: 14px; display: block; }
  .brand-mark {
    position: absolute; left: 512px; top: 116px;
    width: 52px; height: 52px; border-radius: 50%;
    background: var(--maroon);
  }
  .brand-name {
    position: absolute; left: 346px; top: 192px; width: 400px;
    font-family: "Abril Fatface", serif; font-weight: 400; font-size: 56px; line-height: 56px;
    text-align: center;
  }
  .claims {
    position: absolute; left: 346px; top: 325px; width: 400px;
    font-family: "Oswald", sans-serif; font-weight: 500; font-size: 16px;
    line-height: 25px; text-align: center; text-transform: uppercase;
  }
  .instructions { left: 780px; top: 64px; width: 236px; max-height: 180px; overflow: hidden; }
  .instructions .copy { text-align-last: left; }
  .nutrition-panel {
    position: absolute; left: 780px; top: 249px;
    width: 236px; height: 148px; border: 2px solid var(--maroon);
    display: flex; align-items: center; justify-content: center;
    font-size: 9px; font-weight: 700; text-transform: uppercase;
  }
  .uses {
    position: absolute; left: 0; top: 423px; width: 1092px;
    text-align: center; color: var(--white);
    font-family: "Oswald", sans-serif; font-weight: 500;
    font-size: 21px; letter-spacing: 4.6px; text-transform: uppercase;
  }
</style>
</head>
<body>
  <section class="label">
    <svg class="parchment" viewBox="0 0 1092 458" aria-hidden="true">
      <polygon fill="var(--parchment)" points="
        20,44 60,40 120,44 300,38 500,43 700,38 880,43 1040,38 1070,44
        1062,70 1080,80 1062,110 1070,200 1060,260 1072,330 1062,380 1068,410 1040,414
        900,408 700,414 500,406 350,414 200,406 60,414 26,408
        30,380 18,340 30,300 22,250 32,200 20,140 30,100 12,86 30,70"/>
    </svg>

    <div class="panel contact">
      <p class="heading">Company contact details:</p>
      <p class="copy">Lorem ipsum dolor sit amet, consectetur adipisicing elit, sed do eiusmod tempor incididunt ut labore et dolore magna aliqua. Ut enim ad minim veniam, quis nostrud exercitation.</p>
      <p class="copy">Ut enim ad minim veniam, quis nostrud exercitation.Ut enim ad minim veniam, quis nostrud exercitation.</p>
    </div>
    <div class="brand-mini">DUGALD'S<br>BREADS</div>
    <div class="barcode-area">BARCODE</div>

    <div class="brand-mark"></div>
    <div class="count"><span class="num">5</span><span class="unit">PCS</span></div>
    <h1 class="brand-name">DUGALD'S<br>BREADS</h1>
    <p class="claims">Preservative free | 100% natural<br>5 bases | made with olive oil<br>hand made</p>

    <div class="panel instructions">
      <p class="copy"><b>COOKING INSTRUCTIONS:</b> Lorem ipsum dolor sit amet, consectetur adipisicing elit, sed do eiusmod tempor incididunt ut labore et dolore magna aliqua. Ut enim ad minim veniam, quis nostrud exercitation.</p>
      <p class="copy"><b>STORAGE INSTRUCTIONS:</b> Lorem ipsum dolor sit amet, consectetur adipisicing elit, sed do eiusmod.</p>
      <p class="copy"><b>INGREDIENTS:</b> Lorem ipsum dolor sit amet, consectetur adipisicing elit, sed do eiusmod tempor incididunt ut labore et dolore magna aliqua. Ut enim ad minim veniam, quis nostrud exercitation.Lorem ipsum dolor sit amet, consectetur adipisicing elit, sed do eiusmod tempor incididunt ut labore et dolore magna aliqua. Ut enim ad minim veniam, quis nostrud exercitation.</p>
    </div>
    <div class="nutrition-panel">Nutritional information</div>

    <p class="uses">Uses: pizza base, pizza bread, cut toast</p>
  </section>
</body>
</html>
```